Technical Fastener and Industrial Supply Company needs Web Design

Our company is Harlow Rivet & Pin Inc. We serve the OEM Market and have customers across the globe. Custom fastening parts made to print as well as standard fasteners, abrasives, adhesives and vendor managed inventory services. We pride ourselves on reliability, partnership and overall lowest cost of business, with an emphasis on quality and attention to detail. Harlow Rivet does not simply provide products, we provide solutions to save our customers time and money in their supply chain as well as on their assembly lines. Our Customers are in Telecom, Metering, Nuclear, Packaging Equipment, Networking Component, Boat Trailer, Portable Military and Camp Shelters, Knife and Locomotive Heater Industries (varied, but all OEM's). 95% of our customers use Lean and Six Sigma in their operations, and we customize our Vendor Managed Inventory Systems to suit each customer's individual supply chain goals. We have a mechanical engineer on staff who oversees our quality and conformance lab to ensure that customer parts are made to their exacting specifications. We incorporate continuous improvement in every process and task in our business. Texas Orange and Black are the main colors we utilize in our marketing. The final design should communicate reliability, innovation, technical superiority, as well as partnership.

Target Market(s)

Original Equipment Manufacturers - Electronic and Industrial

Industry/Entity Type

Business

Requirements
Must have
• Some animation...eye catching, but not distracting. A contact/request for quote page that connects to a company email address. A balance of graphics, photos and written content. Must be able to edit in Expression Web.

You may use the written content and any photos from our current website www.harlowrivet-example.com
Should not have
• No cartoons, please.

```html
<!DOCTYPE html>
<html lang="en">
<head>
<meta charset="utf-8">
<title>Harlow Rivet Online</title>
<link href="https://fonts.googleapis.com/css2?family=Source+Sans+3:wght@300;400;600&display=swap" rel="stylesheet">
<style>
:root{
  --black:#000000;
  --orange:#f6893a;
  --orange-text:#f07f2a;
  --white:#ffffff;
  --grey-text:#6d6d6d;
  --dark-text:#3a3a3a;
  --card-border:#e2e2e2;
  --footer:#3b3b3b;
  --button:#2a211c;
}
*{margin:0;padding:0;box-sizing:border-box}
html,body{width:1126px;height:1200px;overflow:hidden;background:var(--white)}
body{position:relative;font-family:"Source Sans 3",Arial,sans-serif;color:var(--grey-text)}
.top-band{position:absolute;left:0;top:0;width:1126px;height:487px;background:var(--black)}
.brand{position:absolute;left:88px;top:33px;width:237px;height:66px;border:1px solid #444;display:flex;align-items:center;gap:12px;padding-left:10px}
.brand-mark{width:46px;height:46px;background:var(--orange)}
.brand-name{color:var(--white);font-size:28px;font-weight:400;letter-spacing:.5px}
.main-nav{position:absolute;right:97px;top:66px;display:flex;align-items:center;font-size:19px;color:var(--white)}
.main-nav a,.footer-nav a{color:inherit;text-decoration:none}
.main-nav .sep{margin:0 16px;color:#bbb;font-size:16px}
.hero{position:absolute;left:91px;top:125px;width:944px;height:408px;background:var(--white);box-shadow:0 6px 8px rgba(0,0,0,.12)}
.hero-photo{position:absolute;left:7px;top:7px;width:930px;height:394px;background:linear-gradient(90deg,#7a5a3a 0%,#b89068 25%,#4a3c30 50%,#a88660 75%,#6b5540 100%)}
.hero-caption{position:absolute;left:555px;top:209px;width:390px;height:122px;background:var(--orange);padding:14px 26px;color:var(--white)}
.hero-caption h1{font-size:40px;font-weight:400;line-height:1.1}
.hero-caption p{font-size:14px;line-height:20px;margin-top:4px;font-weight:400}
.hero-dots{position:absolute;left:426px;top:365px;width:92px;height:36px;background:var(--white);border-radius:24px 24px 0 0;display:flex;justify-content:center;align-items:center;gap:4px;padding-top:4px}
.hero-dots span{width:11px;height:11px;border-radius:50%;background:#222}
.features{position:absolute;top:558px;left:91px;display:flex;gap:13px}
.feature-card{position:relative;width:306px;height:184px;border:1px solid var(--card-border);border-radius:3px;background:linear-gradient(#fff 55%,#f1f1f1);padding:20px 25px}
.feature-card h2{color:var(--orange-text);font-size:23px;font-weight:400}
.feature-card p{font-size:13px;line-height:20px;width:150px;margin-top:6px;font-weight:300;color:#777}
.read-more{position:absolute;left:28px;top:120px;width:92px;height:32px;background:var(--button);color:var(--white);font-size:12px;display:flex;align-items:center;justify-content:center;border-radius:2px}
.feature-photo{position:absolute;right:12px;top:52px;width:128px;height:110px;border-radius:8px;background:radial-gradient(#9aa2aa,#e8e8e8 70%,transparent)}
.welcome{position:absolute;left:94px;top:784px;width:565px}
.welcome h2{font-size:31px;font-weight:400;color:#444;margin-bottom:10px}
.welcome p{font-size:13px;line-height:22.5px;color:#555;margin-bottom:9px}
.video{position:absolute;left:690px;top:782px;width:347px;height:232px;border:4px solid #eee}
.video-still{width:100%;height:100%;background:radial-gradient(circle at 45% 45%,#f6c04a,#d67a1a 60%,#9a4a10)}
.play{position:absolute;left:147px;top:89px;width:46px;height:46px;border-radius:50%;background:var(--white)}
.footer{position:absolute;left:0;top:1070px;width:1126px;height:130px;background:var(--footer);color:var(--white)}
.footer-nav{position:absolute;left:94px;top:34px;display:flex;font-size:16px}
.footer-nav .sep{margin:0 14px;color:#bbb}
.copyright{position:absolute;left:96px;top:70px;font-size:13px;color:#ddd;font-weight:300}
.social{position:absolute;left:906px;top:32px;display:flex;gap:7px}
.social span{width:25px;height:25px;border-radius:3px}
</style>
</head>
<body>
<div class="top-band"></div>
<div class="brand"><span class="brand-mark"></span><span class="brand-name">Harlow Rivet</span></div>
<nav class="main-nav">
  <a href="#">Home</a><span class="sep">|</span>
  <a href="#">About Us</a><span class="sep">|</span>
  <a href="#">Products</a><span class="sep">|</span>
  <a href="#">How We Help</a><span class="sep">|</span>
  <a href="#">Contact Us</a>
</nav>

<section class="hero">
  <div class="hero-photo" role="img" aria-label="Warehouse aisle with shelves of boxed fasteners"></div>
  <div class="hero-caption">
    <h1>Harlow Rivet Online</h1>
    <p>Phasellus felis dolor, scelerisque a, tempus eget,<br>lobortis id libero.Donec scelerisque</p>
  </div>
  <div class="hero-dots"><span></span><span></span><span></span><span></span></div>
</section>

<section class="features">
  <article class="feature-card">
    <h2>Why Choose Us</h2>
    <p>Duis tincidunt lectus quis dui viverra vestibulum. Suspendisse</p>
    <a class="read-more">READ MORE</a>
    <div class="feature-photo" role="img" aria-label="Dark nuts and bolts"></div>
  </article>
  <article class="feature-card">
    <h2>Consistent Quality</h2>
    <p>Duis tincidunt lectus quis dui viverra vestibulum. Suspendisse</p>
    <a class="read-more">READ MORE</a>
    <div class="feature-photo" role="img" aria-label="Steel bolts and nuts"></div>
  </article>
  <article class="feature-card">
    <h2>Management Inventory</h2>
    <p>Duis tincidunt lectus quis dui viverra vestibulum. Suspendisse</p>
    <a class="read-more">READ MORE</a>
    <div class="feature-photo" role="img" aria-label="Chrome wrench"></div>
  </article>
</section>

<section class="welcome">
  <h2>Welcome to Harlow Rivet Online</h2>
  <p>Since 1972, Harlow Rivet's mission has been to form strong partnerships with top Inland Northwest companies who share the philosophy of &nbsp;exceptional quality and high integrity.</p>
  <p>We continue to be successful by focusing on our customers' needs by providing many value-added services as well as treating them fairly, ethically and competitively with every transaction. &nbsp;Our VMI (keepfill) programs are electronically set to your maximum desired quantities...we will not overstock your bins. Streamlined operations mean no waiting in line, getting you back on the job quickly to satisfy YOUR customers.</p>
</section>

<div class="video">
  <div class="video-still" role="img" aria-label="Close-up of a nut and bolt in warm orange light"></div>
  <svg class="play" viewBox="0 0 46 46"><circle cx="23" cy="23" r="23" fill="#fff"/><path d="M18 14 L32 23 L18 32 Z" fill="#111"/></svg>
</div>

<footer class="footer">
  <nav class="footer-nav">
    <a href="#">Home</a><span class="sep">|</span>
    <a href="#">About Us</a><span class="sep">|</span>
    <a href="#">Products</a><span class="sep">|</span>
    <a href="#">How We Help</a><span class="sep">|</span>
    <a href="#">Contact Us</a>
  </nav>
  <p class="copyright">Copyright © 2013 Company Name. &nbsp;All right reserved.</p>
  <div class="social">
    <span style="background:#3b5a9a" aria-label="Social link"></span>
    <span style="background:#3fb4e4" aria-label="Social link"></span>
    <span style="background:#1f7bb6" aria-label="Social link"></span>
    <span style="background:#f08a24" aria-label="Feed link"></span>
  </div>
</footer>
</body>
</html>
```